Nutrition Supplements needs Logo and Package Design

We need logo and label design for the new nutrition and dietary supplement brand called "Kelp Horizons".
It is a new brand for western world but is based on 150 year old formulations successfully sold in the East.

The first five formulations are slated to be launched in the US in November.
They will aid in conditions like:
1. Product One: Diabetes,
2. Product Two: Heart Health,
3. Product Three: Men's Health & Vitality,
4. Product Four: Women's Health and Menstrual conditions,
5. Product Five: Sport Nutrition Aid in keeping mind and body agile.

The competition will be Brindle Pantry own brands and brands like Meadow Trail.

All the five products will be packaged in HDPE bottle ( 1 bottle has 60 capsules )
Height / length : 94.5 mm
Width : 51 mm

Please feel free to ask any additional questions.
Updates

Project Deadline Extended
Reason: We are new to this website and modes of operation. We have added participation budget to the project from today. We are also launching a project on pixel forum for website design tomorrow. This website will be for the same products for which this packaging design project is launched. We are excited to find good designers on this platform that we can work with in the long term

Project Deadline Extended

Target Market(s)

Females in the age group 30 - 75.
Aware of nutrition supplements and their benefits, the label will have to stand out when it's next to brands like Brindle Pantry, Meadow trail etc.. in the nutrition isle.
shop at stores like VRT, Brindle Pantry, Internet, Baxter Lou's, Grove Corner.

Industry/Entity Type

Nutrition

Requirements
Nice to have
• It would be nice to have logo design that vibrates combination of freshness, power of traditional remedies, age old secrets, and age defiance.

```html
<!DOCTYPE html>
<html lang="en">
<head>
<meta charset="utf-8">
<title>Fern Sutra – Supplement Labels</title>
<link rel="stylesheet" href="https://fonts.googleapis.com/css2?family=Oswald:wght@500;700&display=swap">
<style>
  :root {
    --canvas: #ffffff;
    --brand-brown: #6b3a1f;
    --brand-mark: #7cb82f;
    --trim: #8a8a8a;
    --pill-top: #ffffff;
    --pill-bottom: #efe7c9;
    --pill-text: #5a3a1e;
    --title: #ffffff;
  }
  * { margin: 0; padding: 0; box-sizing: border-box; }
  html, body { width: 1200px; height: 490px; overflow: hidden; background: var(--canvas); }
  .sheet { position: relative; width: 1200px; height: 490px; font-family: "Oswald", sans-serif; }

  .trim { position: absolute; height: 1px; width: 60px; background: var(--trim); }
  .tick { position: absolute; top: 482px; width: 1px; height: 8px; background: var(--trim); }

  .label { position: absolute; top: 18px; width: 236px; height: 438px; overflow: hidden; }
  .label-bg { position: absolute; inset: 0; }

  .brand-dot {
    position: absolute; top: 24px; left: 50%; width: 26px; height: 26px; margin-left: -13px;
    border-radius: 50%; background: var(--brand-mark);
  }
  .brand {
    position: absolute; top: 56px; left: 0; width: 100%;
    text-align: center; font-weight: 500; font-size: 24px; line-height: 1.2;
    color: var(--brand-brown); letter-spacing: 0.5px;
  }

  .title {
    position: absolute; left: 0; width: 100%; text-align: center;
    color: var(--title); font-weight: 700; text-transform: uppercase; line-height: 1;
    text-shadow: 0 2px 3px rgba(0,0,0,0.35); white-space: nowrap;
  }

  .visual { position: absolute; }

  .count {
    position: absolute; bottom: 0; left: 50%; transform: translateX(-50%);
    width: 120px; height: 30px; border-radius: 15px 15px 0 0;
    background: linear-gradient(var(--pill-top), var(--pill-bottom));
    color: var(--pill-text); font-weight: 500; font-size: 17px;
    text-align: center; line-height: 30px; z-index: 2;
  }
</style>
</head>
<body>
<div class="sheet">

  <div class="trim" style="left:293px;top:18px"></div>
  <div class="trim" style="left:397px;top:18px"></div>
  <div class="trim" style="left:752px;top:18px"></div>
  <div class="trim" style="left:858px;top:18px"></div>
  <div class="trim" style="left:293px;top:456px"></div>
  <div class="trim" style="left:397px;top:456px"></div>
  <div class="trim" style="left:752px;top:456px"></div>
  <div class="trim" style="left:858px;top:456px"></div>
  <div class="tick" style="left:28px"></div>
  <div class="tick" style="left:264px"></div>
  <div class="tick" style="left:486px"></div>
  <div class="tick" style="left:722px"></div>
  <div class="tick" style="left:948px"></div>
  <div class="tick" style="left:1184px"></div>

  <section class="label" style="left:28px">
    <svg class="label-bg" width="236" height="438" viewBox="0 0 236 438">
      <defs>
        <linearGradient id="hdr1" x1="0" y1="0" x2="0" y2="1"><stop offset="0" stop-color="#fff"/><stop offset="1" stop-color="#eef3d9"/></linearGradient>
        <linearGradient id="pnl1" x1="0" y1="0" x2="0" y2="1"><stop offset="0" stop-color="#9bd03c"/><stop offset="1" stop-color="#5fa62a"/></linearGradient>
      </defs>
      <rect width="236" height="438" fill="url(#hdr1)"/>
      <path d="M0 116 Q118 96 236 116 V438 H0 Z" fill="url(#pnl1)"/>
    </svg>
    <span class="brand-dot"></span>
    <div class="brand">Fern Sutra</div>
    <h2 class="title" style="top:138px;font-size:58px">Diabetic</h2>
    <div class="title" style="top:198px;font-size:34px">Multivitamin</div>
    <div class="visual" role="img" aria-label="Basket of fresh fruits and vegetables"
         style="left:14px;top:262px;width:214px;height:126px;border-radius:40px 40px 20px 20px;background:radial-gradient(ellipse at 50% 60%,#d9893a,#7aa83a 60%,rgba(95,166,42,0) 80%)"></div>
    <div class="count">60 CAPSULES</div>
  </section>

  <section class="label" style="left:486px">
    <svg class="label-bg" width="236" height="438" viewBox="0 0 236 438">
      <defs>
        <linearGradient id="hdr2" x1="0" y1="0" x2="0" y2="1"><stop offset="0" stop-color="#fff"/><stop offset="1" stop-color="#eef3d9"/></linearGradient>
        <linearGradient id="pnl2" x1="0" y1="0" x2="0" y2="1"><stop offset="0" stop-color="#ffd27a"/><stop offset="1" stop-color="#f7a73a"/></linearGradient>
      </defs>
      <rect width="236" height="438" fill="url(#hdr2)"/>
      <path d="M0 116 Q118 96 236 116 V438 H0 Z" fill="url(#pnl2)"/>
    </svg>
    <span class="brand-dot"></span>
    <div class="brand">Fern Sutra</div>
    <h2 class="title" style="top:128px;font-size:56px">Heart</h2>
    <div class="title" style="top:184px;font-size:56px">Health</div>
    <div class="visual" role="img" aria-label="Cartoon red heart lifting a barbell"
         style="left:30px;top:250px;width:176px;height:170px;border-radius:50%;background:radial-gradient(circle,#e3262c 0,#c8161d 45%,rgba(247,167,58,0) 70%)"></div>
    <div class="count">60 CAPSULES</div>
  </section>

  <section class="label" style="left:948px">
    <svg class="label-bg" width="236" height="438" viewBox="0 0 236 438">
      <defs>
        <linearGradient id="hdr3" x1="0" y1="0" x2="0" y2="1"><stop offset="0" stop-color="#fff"/><stop offset="1" stop-color="#eef3d9"/></linearGradient>
        <linearGradient id="pnl3" x1="0" y1="0" x2="0" y2="1"><stop offset="0" stop-color="#1f8fe0"/><stop offset="1" stop-color="#2a3f9e"/></linearGradient>
      </defs>
      <rect width="236" height="438" fill="url(#hdr3)"/>
      <path d="M0 116 Q118 96 236 116 V438 H0 Z" fill="url(#pnl3)"/>
    </svg>
    <span class="brand-dot"></span>
    <div class="brand">Fern Sutra</div>
    <h2 class="title" style="top:118px;font-size:38px">Men's</h2>
    <div class="title" style="top:154px;font-size:56px">Health</div>
    <div class="title" style="top:208px;font-size:34px">&amp; Vitality</div>
    <div class="visual" role="img" aria-label="Smiling man in a white sleeveless top, running"
         style="left:40px;top:250px;width:176px;height:188px;border-radius:30px 30px 0 0;background:linear-gradient(160deg,#e7c2a4,#f2f2f2 45%,#2b2b3a 90%);opacity:0.9"></div>
    <div class="count">60 CAPSULES</div>
  </section>

</div>
</body>
</html>
```